Webdesign für Onlineshop
Zielgruppe
Wir verkaufen in unserem Onlineshop alles zum Thema Wohnen mit dem Schwerpunkt Möbel. Die Hauptzielgruppe ist zwischen 25 und 45 Jahren.
Aufgabenstellung
Wir bevorzugen ein modernes, flaches und aufgeräumtes Design ähnlich wie brelk.de / mobvista9.de mit dem Fokus auf Preisaggressivität und Rabatte.
- Das Grundlayout muss so bleiben, wie es aktuell ist. Natürlich dürfen einzelne Elemente verschoben / versetzt werden.
- Im Header sollte Platz für eine kleine Werbefläche sein (ähnlich wie der konfigurierbare Kleiderschrank).
- Der Shop basiert auf Quendrix 1.9.
- Die Rabatte in den Produktdetailseiten müssen genauso aufgebaut sein
- Die Suche sollte in den Header platziert werden und nicht im Menü
- Ein SSL Logo soll im Header platziert weden
- Die Vorteile (Kostenloser Versand, Sicher einkaufen, Kauf auf Rechnung) sollen im Header erscheinen
- Das Design sollte responsive sein
Es wird nur das reine Design ohne Programmierung benötigt.

```html
<!DOCTYPE html>
<html lang="de">
<head>
<meta charset="utf-8">
<title>Produktdetail – Zubehör und ähnliche Artikel</title>
<link href="https://fonts.googleapis.com/css2?family=Open+Sans:wght@300;400;600;700&display=swap" rel="stylesheet">
<style>
:root{
  --teal:#3fa3bd;
  --green:#8aa63b;
  --ink:#222;
  --text:#444;
  --muted:#7a7a7a;
  --line:#e2e2e2;
  --tile:#efefef;
  --panel:#f6f8f9;
}
*{box-sizing:border-box;margin:0;padding:0}
html,body{width:954px;height:1200px;overflow:hidden;background:#fff}
body{font-family:'Open Sans',sans-serif;color:var(--text);position:relative}
.abs{position:absolute}

/* contact strip */
.contact{left:134px;top:-2px;width:492px;height:92px;border:1px solid var(--line);border-radius:0 0 4px 4px}
.contact-title{left:25px;top:14px;font-size:9px;color:var(--ink)}
.phone-icon{left:23px;top:38px}
.phone-number{left:50px;top:36px;font-size:14.5px;font-weight:700;color:var(--green)}
.phone-hours{left:50px;top:55px;font-size:5.5px;color:var(--ink)}
.field{border:1px solid #ddd;border-radius:3px;font-size:6.5px;color:#bbb;padding:4px 8px}
.field-mail{left:196px;top:5px;width:175px;height:18px}
.field-msg{left:196px;top:25px;width:175px;height:33px}
.send-btn{left:197px;top:61px;width:107px;height:17px;background:var(--teal);color:#fff;font-size:6.5px;font-weight:600;letter-spacing:.3px;display:flex;align-items:center;justify-content:center;border-radius:2px}
.agent{left:374px;top:2px;width:108px;height:88px;background:linear-gradient(180deg,#f1ece7,#f7f7f9 60%,#eef1f5)}

.ship{left:657px;top:14px;display:flex;align-items:center;gap:14px;font-size:8.5px;color:var(--ink)}
.ship-rule{left:656px;top:44px;width:161px;height:1px;background:var(--line)}
.share-row{left:658px;top:62px;display:flex;gap:4px}
.share-btn{border:1px solid var(--line);color:var(--text);font-size:7.5px;height:14px;padding:0 6px;display:flex;align-items:center;border-radius:2px;background:#fff}
.share-btn b{font-weight:400;color:var(--muted);margin-left:4px}

/* sections */
.section-title{font-size:19.5px;font-weight:300;color:var(--ink);letter-spacing:.2px}
.nav-btn{width:36px;height:36px;border:1px solid var(--line);border-radius:50%;display:flex;align-items:center;justify-content:center}
.card{width:162px}
.card-media{width:162px;height:111px;background:var(--tile)}
.card-name{margin:11px 10px 0;font-size:10.5px;font-weight:300;line-height:14px;color:var(--ink);height:28px}
.card-row{display:flex;align-items:center;justify-content:space-between;margin:13px 7px 0 10px}
.price{font-size:16.5px;color:var(--ink)}
.price.sale{color:var(--teal)}
.qty{display:flex;gap:3px}
.qty-val{width:26px;height:25px;border:1px solid var(--line);border-radius:2px;font-size:10px;display:flex;align-items:center;justify-content:center;color:var(--ink)}
.qty-steps{width:12px;height:25px;border:1px solid var(--line);border-radius:2px;display:flex;flex-direction:column;align-items:center;justify-content:space-around;font-size:9px;line-height:1;color:#999;font-weight:300}
.badge{width:42px;height:42px;border-radius:50%;background:var(--teal);color:#fff;font-size:12.5px;font-weight:600;display:flex;align-items:center;justify-content:center}
.old-price{font-size:8.5px;text-decoration:line-through;color:var(--ink);margin:10px 10px 0}

/* description */
.desc{left:133px;top:421px;width:495px}
.desc h3{font-size:13px;font-weight:400;color:var(--ink);margin:14px 0 14px}
.desc p{font-size:8.4px;line-height:13.3px;color:var(--muted);margin-bottom:7px}
.desc h4{font-size:8.8px;font-weight:400;color:var(--ink);margin:15px 0 10px}
.desc ul{list-style:none}
.desc li{font-size:8.6px;color:var(--ink);height:19.2px;padding-left:9px;position:relative}
.desc li::before{content:"";position:absolute;left:1px;top:4px;width:3px;height:3px;background:var(--teal)}

.facts{left:656px;top:423px;width:162px;height:328px;background:var(--panel);border-radius:3px;padding:11px 13px}
.facts h5{font-size:8px;font-weight:400;color:var(--teal);margin-bottom:8px}
.facts ul{list-style:none}
.facts li{font-size:7px;line-height:12px;color:var(--ink);padding-left:10px;position:relative;margin-bottom:2.5px;overflow-wrap:anywhere}
.facts li::before{content:"";position:absolute;left:1px;top:5px;width:2.5px;height:2.5px;border-radius:50%;background:var(--teal)}
.facts hr{border:0;border-top:1px solid #e0e0e0;margin:10px 0 12px}
.facts .note{font-size:7px;line-height:12px;color:var(--muted);margin-top:8px}
.doc{display:flex;gap:9px;align-items:center;font-size:7px;line-height:11px;color:var(--ink)}
.doc-icon{width:20px;height:20px;border:1px solid #ddd;border-radius:2px;display:flex;align-items:center;justify-content:center;background:#fff}
</style>
</head>
<body>

<!-- contact strip -->
<div class="abs contact">
  <div class="abs contact-title">Sie haben Fragen?</div>
  <svg class="abs phone-icon" width="22" height="22" viewBox="0 0 22 22" fill="none" stroke="#8aa63b" stroke-width="1.3">
    <circle cx="11" cy="11" r="10"/>
    <path d="M7.5 6.5l2 2-1.2 1.4a7 7 0 0 0 3.8 3.8l1.4-1.2 2 2-1.3 1.4c-3.5 0-7.8-4.3-7.9-7.9z"/>
  </svg>
  <div class="abs phone-number">0521 / 47 12 36 90</div>
  <div class="abs phone-hours">Mo-Fr 9-21 Uhr&nbsp;&nbsp; Sa 10-15 Uhr</div>
  <div class="abs field field-mail">Ihre E-mail adresse</div>
  <div class="abs field field-msg">Ihre Nachricht</div>
  <div class="abs send-btn">NACHRICHT VERSENDEN</div>
  <div class="abs agent" role="img" aria-label="Kundenberaterin mit Headset"></div>
</div>

<div class="abs ship">
  <svg width="15" height="10" viewBox="0 0 15 10"><rect width="15" height="10" fill="#e3262e"/><rect x="6.3" y="2" width="2.4" height="6" fill="#fff"/><rect x="4.5" y="3.8" width="6" height="2.4" fill="#fff"/></svg>
  <span>Wir liefern nach Schweiz&nbsp;&nbsp;›</span>
</div>
<div class="abs ship-rule"></div>
<div class="abs share-row"><span class="share-btn">Gefällt mir<b>109</b></span><span class="share-btn">Teilen</span></div>

<!-- Passendes Zubehör carousel -->
<h2 class="abs section-title" style="left:134px;top:137px">PASSENDES ZUBEHÖR</h2>
<div class="abs nav-btn" style="left:736px;top:134px"><svg width="12" height="10" viewBox="0 0 12 10" fill="none" stroke="#555" stroke-width="1.1"><path d="M11 5H1M5 1L1 5l4 4"/></svg></div>
<div class="abs nav-btn" style="left:782px;top:134px"><svg width="12" height="10" viewBox="0 0 12 10" fill="none" stroke="#555" stroke-width="1.1"><path d="M1 5h10M7 1l4 4-4 4"/></svg></div>

<div class="abs card" style="left:136px;top:185px">
  <div class="card-media" role="img" aria-label="Zwei Einlegeböden"></div>
  <div class="card-name">Einlegeboden 2er-Satz,<br>Maße: B/H/T/ ca. 110/2/50</div>
  <div class="card-row"><span class="price">54,95 €</span><div class="qty"><div class="qty-val">1</div><div class="qty-steps"><span>+</span><span>–</span></div></div></div>
</div>
<div class="abs card" style="left:309px;top:185px">
  <div class="card-media" role="img" aria-label="Kleiderstange mit Halterung"></div>
  <div class="card-name">Boxspringbett schwarz,<br>Feinstrukturstoff</div>
  <div class="card-row"><span class="price">119,95 €</span><div class="qty"><div class="qty-val">1</div><div class="qty-steps"><span>+</span><span>–</span></div></div></div>
</div>
<div class="abs card" style="left:483px;top:185px">
  <div class="card-media" role="img" aria-label="Schmale Kommode schwarz mit Schubladen" style="background:linear-gradient(90deg,#efefef 40%,#3a3a3a 40%,#2a2a2a 63%,#efefef 63%)"></div>
  <div class="card-name">Boxspringbett schwarz,<br>Feinstrukturstoff</div>
  <div class="card-row"><span class="price sale">79,95 €</span><div class="qty"><div class="qty-val">1</div><div class="qty-steps"><span>+</span><span>–</span></div></div></div>
</div>
<div class="abs badge" style="left:477px;top:179px">-17%</div>
<div class="abs card" style="left:656px;top:185px">
  <div class="card-media" role="img" aria-label="Sideboard in Nussbaum" style="background:linear-gradient(180deg,#efefef 17%,#6b4a36 17%,#5a3c2b 83%,#efefef 83%)"></div>
  <div class="card-name">Boxspringbett schwarz,<br>Feinstrukturstoff</div>
  <div class="card-row"><span class="price">159,95 €</span><div class="qty"><div class="qty-val">1</div><div class="qty-steps"><span>+</span><span>–</span></div></div></div>
</div>

<!-- description -->
<div class="abs desc">
  <h2 class="section-title">PASSENDES ZUBEHÖR</h2>
  <h3>Freuen Sie sich auf ein wirkungsvolles Schlafzimmer</h3>
  <p>Dieses Schlafzimmer lädt Sie täglich zum Entspannen ein. Es ist das gradlinige Design in Kombination mit dem Trenddekor Columbia Nussbaum-Nachbildung, dass dieses Schlafzimmer ansprechend wirken lässt. Freuen Sie sich auf einen modernen Look, indem Sie sich umgehend wohlfühlen.</p>
  <p>Das Schlafzimmer besteht aus einem Schwebetürenschrank, einem Bett und 2 Nachtschränken. In dem Schrank sowie den Nachtschränken erhalten Sie einen großzügigen Stauraum, der es Ihnen ermöglicht sich durchdacht einzurichten. Für weitere Unterbringungsmöglichkeiten können Sie diese Zusammenstellung um weitere Möbelstücke erweitern wählen Sie verschiedenste Kombinationen aus unserem umfangreichen Typenplan. Auch im Punkte Holzdekore und Absetzungen stehen Ihnen zahlreiche Varianten zur Verfügung. Rundum ein exzellentes Schlafzimmer.</p>
  <h4>Allgemeines</h4>
  <ul>
    <li>Schwebetürenschrank mit Absetzungen aus Glas in schwarz</li>
    <li>Bett mit Metallfüßen in aluminiumfarben (ohne Matratzen und Lattenrost)</li>
    <li>2 Nachtschränke mit je 2 Schubkästen</li>
    <li>stabile Ausführung</li>
    <li>deutscher Hersteller und deutsche Produktion</li>
  </ul>
</div>

<aside class="abs facts">
  <h5>Abmessungen im Detail (B/H/T ca.)</h5>
  <ul>
    <li>Schwebetürenschrank:<br>225/210/65 cm</li>
    <li>Bett:188/38/208 cm</li>
    <li>Liegefläche: 180 x 200 cm</li>
    <li>2 Nachtschränke: je 52/40/38 cm</li>
  </ul>
  <hr>
  <h5>Lieferumfang</h5>
  <ul>
    <li>Schwebetürenschrank</li>
    <li>Bett</li>
    <li>2 Nachtschränke</li>
    <li>ohne evtl. zusätzlich abgebildete Dekorationen/Zubehörartikel/Ergänzungen</li>
  </ul>
  <div class="note">Ware zerlegt zum Selbstaufbau (inkl. detaillierter Anleitung)</div>
  <hr>
  <h5>Anleitungen und Dokumente</h5>
  <div class="doc">
    <div class="doc-icon"><svg width="10" height="11" viewBox="0 0 10 11" fill="none" stroke="#3fa3bd" stroke-width=".9"><path d="M1 .5h5.5L9 3v7.5H1z"/><path d="M3 8.5c1-2 2-4 2-5.5M2.8 7.5h4.4"/></svg></div>
    <span>Typenplan zum Download<br>(PDF-Datei) - 330Kb</span>
  </div>
</aside>

<!-- Ähnliche Artikel -->
<h2 class="abs section-title" style="left:134px;top:782px">ÄHNLICHE ARTIKEL</h2>
<div class="abs nav-btn" style="left:736px;top:779px"><svg width="12" height="10" viewBox="0 0 12 10" fill="none" stroke="#555" stroke-width="1.1"><path d="M11 5H1M5 1L1 5l4 4"/></svg></div>
<div class="abs nav-btn" style="left:782px;top:779px"><svg width="12" height="10" viewBox="0 0 12 10" fill="none" stroke="#555" stroke-width="1.1"><path d="M1 5h10M7 1l4 4-4 4"/></svg></div>

<div class="abs card" style="left:136px;top:830px">
  <div class="card-media" role="img" aria-label="Weißes Bett mit roter Bettwäsche" style="background:linear-gradient(180deg,#e8e8e8 30%,#3a3a3a 30%,#3a3a3a 42%,#b3262c 42%,#9c1e24 75%,#eaeaea 75%)"></div>
  <div class="card-name">Wohnlandschaft, in<br>Mikrofaser Vintage-Look</div>
  <div class="old-price">999,00 €</div>
  <div class="price sale" style="margin:1px 10px 0">575,10 €</div>
</div>
<div class="abs badge" style="left:131px;top:824px">-36%</div>
<div class="abs card" style="left:309px;top:830px">
  <div class="card-media" role="img" aria-label="Schlafzimmer mit Holzbett und Fensterfront" style="background:linear-gradient(180deg,#a7a59a,#d9c9b1 45%,#c9a999 60%,#7a6c60)"></div>
  <div class="card-name">Boxspringbett schwarz,<br>Feinstrukturstoff</div>
  <div class="price" style="margin:21px 10px 0">575,10 €</div>
</div>
<div class="abs card" style="left:483px;top:830px">
  <div class="card-media" role="img" aria-label="Kleiderschrank aus massivem Holz" style="background:linear-gradient(90deg,#7b6a4a,#c59a62 30%,#b08452 60%,#a27a4d)"></div>
  <div class="card-name">Boxspringbett schwarz,<br>Feinstrukturstoff</div>
  <div class="price" style="margin:21px 10px 0">575,10 €</div>
</div>
<div class="abs card" style="left:656px;top:830px">
  <div class="card-media" role="img" aria-label="Schwarzes Boxspringbett im hellen Raum" style="background:linear-gradient(180deg,#dedede 35%,#f0f0f0 45%,#333 60%,#2a2a2a 88%,#b8b33a 88%)"></div>
  <div class="card-name">Boxspringbett schwarz,<br>Feinstrukturstoff</div>
  <div class="price" style="margin:21px 10px 0">575,10 €</div>
</div>

<!-- Ebenfalls interessant -->
<h2 class="abs section-title" style="left:133px;top:1071px">EBENFALLS INTERESSANT</h2>
<div class="abs nav-btn" style="left:735px;top:1068px"><svg width="12" height="10" viewBox="0 0 12 10" fill="none" stroke="#555" stroke-width="1.1"><path d="M11 5H1M5 1L1 5l4 4"/></svg></div>
<div class="abs nav-btn" style="left:781px;top:1068px"><svg width="12" height="10" viewBox="0 0 12 10" fill="none" stroke="#555" stroke-width="1.1"><path d="M1 5h10M7 1l4 4-4 4"/></svg></div>

<div class="abs card-media" style="left:135px;top:1119px;height:81px;background:linear-gradient(135deg,#8f7b4c,#c8a66c 50%,#e7e2d6)" role="img" aria-label="Nachttisch und Bett aus Holz"></div>
<div class="abs card-media" style="left:308px;top:1119px;height:81px;background:linear-gradient(180deg,#cfcfd0,#a9a9ab 50%,#8d8d90)" role="img" aria-label="Graues Boxspringbett mit Decke"></div>
<div class="abs card-media" style="left:482px;top:1119px;height:81px;background:linear-gradient(90deg,#e6e3dc 35%,#8a7355 35%,#4a4540 60%,#a58a64)" role="img" aria-label="Schrank mit Spiegeltüren"></div>
<div class="abs card-media" style="left:655px;top:1119px;height:81px;background:linear-gradient(90deg,#3b3b3b 45%,#eaeaea 45%,#eaeaea 70%,#b0252b 70%)" role="img" aria-label="Nachtkommode und Bett mit roter Decke"></div>

</body>
</html>
```